Business Card Design for Cybersecurity Company - Quorvent Systems

We need a business card design for our new cybersecurity company, Quorvent. We’re going for a clean, hi tech look that feels modern, premium, and trustworthy. We want a design that really stands out and makes people say WOW when we hand it over!

Quorvent delivers reliable IT support and managed services for small and mid sized businesses. We help companies stay secure, efficient, and connected through proactive monitoring, cybersecurity services, cloud management, and remote support.

Target Market(s)

Designers should target small and mid sized businesses that need dependable cybersecurity and IT support.

Industry/Entity Type

Cybersecurity, Managed Service Provider, IT services

Contact Information for Business Card

Contact information

Requirements
Must have
• The card should look clean, modern, and tech focused, with the Quorvent logo, clear contact info, and strong readability. It needs to feel premium and professional while still keeping a simple layout that fits a cybersecurity and IT brand.
Nice to have
• Nice to have elements include subtle touches that give the card a modern, tech feel, along with a layout that works well in different background styles.
Should not have
• The card should avoid clutter, loud graphics, or anything that takes attention away from the logo and contact details.

```html
<!DOCTYPE html>
<html lang="en">
<head>
<meta charset="utf-8">
<title>Quorvent Systems — Business Card</title>
<link rel="stylesheet" href="https://fonts.googleapis.com/css2?family=Montserrat:wght@400;500;700&display=swap">
<style>
  :root {
    --backdrop: #3f3631;
    --card-dark: #212121;
    --brand-violet: #6a4ea1;
    --brand-indigo: #5060b0;
    --brand-blue: #3c82c6;
    --ink-light: #ffffff;
    --ink-muted: rgba(255, 255, 255, 0.62);
  }
  * { margin: 0; padding: 0; box-sizing: border-box; }
  html, body {
    width: 1200px;
    height: 1200px;
    overflow: hidden;
    background: var(--backdrop);
    font-family: "Montserrat", Arial, sans-serif;
  }
  .canvas {
    position: relative;
    width: 1200px;
    height: 1200px;
  }
  .card {
    position: absolute;
    left: 179px;
    width: 862px;
    height: 495px;
  }
  .card-front {
    top: 85px;
    background: var(--card-dark);
    display: flex;
    align-items: center;
    justify-content: center;
  }
  .brand-lockup {
    display: flex;
    align-items: center;
    gap: 18px;
  }
  .brand-dot {
    width: 22px;
    height: 22px;
    border-radius: 50%;
    background: var(--brand-blue);
  }
  .brand-name {
    font-weight: 500;
    font-size: 46px;
    letter-spacing: 1px;
    color: var(--brand-indigo);
  }
  .card-back {
    top: 622px;
    background: linear-gradient(90deg, var(--brand-violet) 0%, var(--brand-indigo) 45%, var(--brand-blue) 100%);
    color: var(--ink-light);
  }
  .holder-name {
    position: absolute;
    left: 47px;
    top: 40px;
    font-weight: 700;
    font-size: 36px;
    letter-spacing: 0.3px;
  }
  .holder-role {
    position: absolute;
    left: 47px;
    top: 92px;
    font-weight: 400;
    font-size: 21px;
    color: var(--ink-muted);
  }
  .contact-list {
    position: absolute;
    left: 46px;
    top: 317px;
    list-style: none;
  }
  .contact-list li {
    font-size: 22px;
    font-weight: 400;
    line-height: 38px;
    letter-spacing: 0.5px;
  }
  .contact-label {
    font-weight: 700;
    margin-right: 6px;
  }
</style>
</head>
<body>
  <main class="canvas">
    <section class="card card-front" aria-label="Card front">
      <div class="brand-lockup">
        <span class="brand-dot" aria-hidden="true"></span>
        <span class="brand-name">Quorvent Systems</span>
      </div>
    </section>

    <section class="card card-back" aria-label="Card back">
      <h1 class="holder-name">Dorian Hale</h1>
      <p class="holder-role">Owner | CEO | Quorvent Systems</p>
      <ul class="contact-list">
        <li><span class="contact-label">P:</span>(855) 410-7720</li>
        <li><span class="contact-label">M:</span>(813) 555-0187</li>
        <li><span class="contact-label">E:</span>dorian@quorvent.com</li>
        <li><span class="contact-label">W:</span>quorvent.com</li>
      </ul>
    </section>
  </main>
</body>
</html>
```